Classic and neutral book cover design

We are looking for a classic and neutral book cover design to be used as the template for a series of books to be published. We are hence looking for a template that will allow us to easily change the title name for all books in this series.
The use of very few colours (black and white is welcome) and few design elements is a big bonus. As a source of inspiration we would like to ask you to view the very simple and
If you think you have a cool idea that can add a twist to the formal classic look don't hesitate. Go for it !
Work will be done for a 30 year old Sweden based cultural non-profit called VĂ©lra (www.velrafoundation.example). We work with the publishing and supporting of post-modern art and literature addressing contemporary topics but are also involved in assisting projects of cultural preservation.
Target Market(s)
The audience is expected to have some form of interest in culture but could range from hobbyist readers to tenure track scholars
Industry/Entity Type
Non-Profit
Requirements
Must have
- General:
- Classic and neutral feel
- Preferably very simple and few shapes
- usage of few colours (black and white is welcome)
Information to be displayed on the cover is:
- Author
- Title
- type of work e.g. play/novel (optional)
- publishing house (in this case "Velra Publishing")
Nice to have
- ideas to prevent it from become boring are of course welcome
Should not have
- - too many colours

```html
<!DOCTYPE html>
<html lang="en">
<head>
<meta charset="utf-8">
<title>Anders Holmvik – Miss Elise · Velra Publishing</title>
<link rel="stylesheet" href="https://fonts.googleapis.com/css2?family=Cinzel:wght@400&family=Pinyon+Script&family=Cormorant+Garamond:wght@600&display=swap">
<style>
  :root {
    --backdrop: #b4b4b4;
    --paper: #ffffff;
    --ink: #111111;
    --author-grey: #8e8e8e;
    --shadow: rgba(0, 0, 0, 0.28);
  }
  html, body {
    margin: 0;
    padding: 0;
    width: 1200px;
    height: 812px;
    overflow: hidden;
    background: var(--backdrop);
  }
  .stage {
    position: relative;
    width: 1200px;
    height: 812px;
  }
  .book-cover {
    position: absolute;
    left: 351px;
    top: 83px;
    width: 498px;
    height: 646px;
    background: var(--paper);
    box-shadow: 4px 5px 6px var(--shadow);
    transform: scale(1.1);
    transform-origin: center;
  }
  .rule {
    position: absolute;
    left: 0;
    background: var(--ink);
  }
  .rule--top-thick { top: 11px; width: 373px; height: 3px; }
  .rule--top-thin  { top: 18px; width: 373px; height: 1px; }
  .rule--bottom-thin  { top: 625px; width: 490px; height: 1px; }
  .rule--bottom-thick { top: 630px; width: 490px; height: 3px; }

  .publisher {
    position: absolute;
    right: 8px;
    top: 10px;
    margin: 0;
    font-family: "Cormorant Garamond", serif;
    font-weight: 600;
    font-size: 10.5px;
    letter-spacing: 0.04em;
    color: var(--ink);
    line-height: 1;
  }
  .author {
    position: absolute;
    right: 5px;
    top: 160px;
    margin: 0;
    font-family: "Cinzel", serif;
    font-weight: 400;
    color: var(--author-grey);
    text-align: left;
    line-height: 1;
  }
  .author__first {
    display: block;
    margin-left: 28px;
    font-size: 26px;
    letter-spacing: 0.01em;
  }
  .author__first .initial { font-size: 33px; }
  .author__last {
    display: block;
    margin-top: -4px;
    font-size: 40px;
    letter-spacing: 0.01em;
  }
  .author__last .initial { font-size: 52px; }

  .title {
    position: absolute;
    right: 8px;
    top: 508px;
    margin: 0;
    font-family: "Pinyon Script", cursive;
    font-weight: 400;
    font-size: 44px;
    color: var(--ink);
    line-height: 1.2;
  }
</style>
</head>
<body>
  <main class="stage">
    <article class="book-cover">
      <div class="rule rule--top-thick"></div>
      <div class="rule rule--top-thin"></div>
      <p class="publisher">VELRA PUBLISHING</p>

      <h2 class="author">
        <span class="author__first"><span class="initial">A</span>NDERS</span>
        <span class="author__last"><span class="initial">H</span>OLMVIK</span>
      </h2>

      <h1 class="title">Miss Elise</h1>

      <div class="rule rule--bottom-thin"></div>
      <div class="rule rule--bottom-thick"></div>
    </article>
  </main>
</body>
</html>
```